Condo Debts Collection Business needs a Web Design (Contest)

I need a site for a client, who works with condo debts collection, and ensure all revenues provided by condo fees will be always available to the building manager of condo on a specific date, regardless of defaults.I have the logo of the companies, and some requirements on layout (kind of slider, menu options, phone number on a noble position, etc).
Updates

Designs look the same

Target Market(s)

I have two targets for this design: - Condominium's building manager. This target is looking for a solution to overdue debts on it's condo. - Residents on condominiums. This target wants to live in a better place, where their neighbors pay their condominium fees on time.

Number of Pages Required

1 page

Requirements
Must have
• - Slider with title, some short text related, a nice image (I prefer happy and/or peaceful family, people doing business, happy friends, and so on).
• - I have a special attention to menu. I'm looking for one I can have a nice effect, more elegant, charming, kind of innovative.
• - Phone number on the top (or clearly visible).
• - Member log in area or icon on the top (or clearly visible).
• - News/articles area.
• - Modern fonts, with good quality, sans-serif on areas where reading is more intensive (prefer Google web-fonts).
• - Colors specified on attached files.
• - Header similar or inspired by the "FILE 3"
Nice to have
• - Clear background color, cause it's better to read larger texts (like articles). Dark backgrounds makes reading difficult.
• - A site with effects (like shadows, lines, gradients, lights) is usually pretty.
• - I pay attention on beautiful footers.
Should not have
• - Images with a lot of money (I don't sell richness, I sell tranquility, peace, harmony, safety).
• - Poor menu.
• - Lots of curves. My customer asked for straight lines.

```html
<!DOCTYPE html>
<html lang="en">
<head>
<meta charset="utf-8">
<title>Serenia – Condo Fee Guarantee</title>
<link rel="stylesheet" href="https://fonts.googleapis.com/css2?family=Montserrat:wght@400;600;700&family=Open+Sans:wght@400;600&display=swap">
<style>
:root{
  --navy:#1b2c5c;
  --navy-deep:#142249;
  --orange:#f36f21;
  --orange-dark:#d9561a;
  --ink:#2c3442;
  --muted:#7a808a;
  --line:#e3e6ea;
  --pale:#f3f4f6;
  --white:#ffffff;
}
*{box-sizing:border-box;margin:0;padding:0}
html,body{width:1200px;height:4836px;overflow:hidden}
body{font-family:"Open Sans",Arial,sans-serif;color:var(--ink);background:var(--white);font-size:14px;line-height:1.7}
h1,h2,h3,h4,.nav,.btn{font-family:"Montserrat",Arial,sans-serif}
.section-title{text-align:center;font-size:40px;line-height:1.2;font-weight:400;color:var(--navy);letter-spacing:1px}
.section-title span{color:var(--orange);font-weight:700}
.section-sub{text-align:center;color:var(--muted);font-size:13px;line-height:1.5;margin-top:10px}
.btn{display:inline-block;font-size:11px;line-height:1.5;font-weight:600;letter-spacing:.5px;border-radius:16px;padding:7px 20px}
.btn-solid{background:var(--orange);color:var(--white)}
.btn-outline{border:1px solid var(--orange);color:var(--orange)}
.ph{display:block}

/* header */
.site-header{position:relative;height:112px;background:var(--navy-deep)}
.brand{position:absolute;left:96px;top:22px;display:flex;align-items:center;gap:12px;font-family:"Montserrat",sans-serif;font-weight:700;font-size:30px;line-height:1.2;color:var(--white);letter-spacing:1px}
.brand-mark{width:30px;height:30px;background:var(--orange)}
.topbar-right{position:absolute;right:96px;top:18px;display:flex;align-items:center;gap:22px;color:var(--white);font-size:13px;font-weight:600}
.topbar-right .phone{display:flex;align-items:center;gap:8px}
.nav{position:absolute;left:520px;right:0;top:72px;height:40px;background:linear-gradient(90deg,var(--orange),var(--orange-dark));display:flex;align-items:center;gap:34px;padding-left:28px;color:var(--white);font-size:12px;font-weight:600}
.nav .active{background:var(--white);color:var(--orange);padding:4px 12px;line-height:1.4}

/* hero */
.hero{position:relative;height:600px;background:linear-gradient(120deg,#56637c,#8a96a8 45%,#3f4b63)}
.hero-copy{position:absolute;left:110px;top:230px;width:440px;color:var(--white)}
.hero-copy h1{font-size:52px;line-height:1.3;font-weight:600;letter-spacing:2px;background:rgba(20,34,73,.35);padding:0 6px;display:inline-block}
.hero-copy p{font-size:13px;margin:12px 0 20px}
.hero-dots{position:absolute;left:400px;top:560px;display:flex;gap:8px}
.hero-dots i{width:10px;height:10px;border-radius:50%;border:2px solid var(--white)}
.hero-dots i:first-child{background:var(--white)}

/* services */
.services{height:508px;padding-top:100px}
.service-grid{display:flex;justify-content:center;gap:90px;margin-top:60px}
.service{width:240px;text-align:center}
.service h3{font-size:14px;color:var(--navy);margin:18px 0 10px}
.service p{font-size:12px;color:var(--muted);margin-bottom:18px}

/* about */
.about{position:relative;height:480px;background:var(--pale)}
.about .ph{position:absolute;left:0;top:0;width:580px;height:480px;background:linear-gradient(135deg,#b9bfc8,#6c7788)}
.about-copy{position:absolute;left:630px;top:60px;width:470px}
.about-copy h2{font-size:40px;line-height:1.2;font-weight:400;color:var(--navy)}
.about-copy h2 span{color:var(--orange);font-weight:700}
.about-copy p{font-size:12px;color:var(--muted);margin-top:18px}

/* video */
.video{position:relative;height:580px;background:linear-gradient(180deg,var(--orange) 0,var(--orange-dark) 120px,#eef0f3 120px)}
.video .section-title{color:var(--white);padding-top:26px}
.video .section-sub{color:#ffe4d2;margin-top:8px}
.video-frame{position:absolute;left:170px;top:146px;width:860px;height:410px;background:linear-gradient(120deg,#5d6a80,#a4aebb 50%,#4d5a70)}
.video-frame svg{position:absolute;left:400px;top:175px}

/* what we do */
.what{position:relative;height:480px}
.what-copy{position:absolute;left:110px;top:100px;width:420px}
.what-copy h2{font-size:40px;line-height:1.2;font-weight:400;color:var(--navy)}
.what-copy h2 span{color:var(--orange);font-weight:700}
.what-copy p{font-size:12px;color:var(--muted);margin-top:18px}
.what .ph{position:absolute;left:570px;top:60px;width:520px;height:340px;background:linear-gradient(135deg,#3a4a6e,#9aa4b6 55%,#5b6884)}

/* news */
.news{height:660px;background:var(--white);padding-top:40px;border-top:1px solid var(--line)}
.news-grid{display:flex;justify-content:center;gap:30px;margin-top:50px}
.card{width:300px;border:1px solid var(--line);background:var(--white)}
.card .ph{height:210px;background:linear-gradient(135deg,#a9b1bd,#6a768a)}
.card-body{padding:18px 14px 20px}
.card small{font-size:11px;color:var(--muted)}
.card h4{font-size:13px;color:var(--navy);margin:8px 0;line-height:1.5}
.card p{font-size:12px;color:var(--muted);margin-bottom:14px}

/* testimonials */
.testimonials{height:600px;background:linear-gradient(180deg,#eceef2,#f6f7f9);padding-top:60px}
.quote-grid{display:flex;justify-content:center;gap:40px;margin-top:60px}
.quote{width:430px}
.quote-box{border:1px dashed #c9ced6;padding:24px 26px;background:var(--white);font-size:12px;color:var(--muted)}
.stars{color:var(--orange);font-size:14px;letter-spacing:2px;display:block;margin-bottom:6px}
.stars b{color:var(--navy);font-size:20px;margin-right:8px}
.author{display:flex;align-items:center;gap:14px;margin:22px 0 0 80px}
.avatar{width:60px;height:60px;border-radius:50%;background:linear-gradient(135deg,#b0b7c2,#6f7a8c)}
.author h4{font-size:12px;color:var(--navy)}
.author small{font-size:11px;color:var(--muted)}

/* location */
.location{position:relative;height:280px}
.map{position:absolute;left:110px;top:20px;width:570px;height:240px;background:linear-gradient(135deg,#e7e3d8,#d3dde6)}
.map-card{position:absolute;left:160px;top:60px;width:200px;background:var(--white);padding:16px;box-shadow:0 3px 10px rgba(0,0,0,.15)}
.map-card h4{font-size:13px;color:var(--navy)}
.map-card p{font-size:11px;color:var(--muted)}
.location .photo{position:absolute;left:700px;top:20px;width:390px;height:240px;background:linear-gradient(135deg,#9ea7b4,#5f6b80)}

/* footer */
.site-footer{height:536px;background:var(--navy-deep);border-top:6px solid var(--orange);color:#c9d0de;position:relative}
.footer-cols{display:flex;gap:60px;padding:60px 110px 0}
.footer-col h4{color:var(--white);font-size:14px;margin-bottom:18px}
.footer-col{font-size:12px}
.footer-col ul{list-style:none}
.footer-col li{margin-bottom:8px}
.footer-col li::before{content:"› ";color:var(--orange)}
.col-contact{width:200px}
.col-links{width:140px}
.col-res{width:180px}
.col-news{width:260px}
.contact-line{display:flex;gap:10px;margin-bottom:10px}
.newsletter-input{height:34px;background:var(--white);margin:14px 0 12px;color:var(--muted);padding:6px 10px;font-size:11px}
.socials{position:absolute;left:0;right:0;top:360px;display:flex;justify-content:center;gap:12px}
.socials i{width:30px;height:30px;border-radius:50%;border:1px solid #c9d0de}
.copyright{position:absolute;left:0;right:0;bottom:0;height:56px;background:#0f1a3a;text-align:center;line-height:56px;font-size:12px}
</style>
</head>
<body>

<header class="site-header">
  <div class="brand"><span class="brand-mark"></span>SERENIA</div>
  <div class="topbar-right">
    <span class="phone">
      <svg width="16" height="16" viewBox="0 0 24 24" fill="#f36f21"><path d="M6.6 10.8a15 15 0 0 0 6.6 6.6l2.2-2.2c.3-.3.7-.4 1-.2 1.1.4 2.3.6 3.6.6.6 0 1 .4 1 1V20c0 .6-.4 1-1 1A17 17 0 0 1 3 4c0-.6.4-1 1-1h3.5c.6 0 1 .4 1 1 0 1.3.2 2.5.6 3.6.1.3 0 .7-.2 1z"/></svg>
      CALL US : (555) 013-4782
    </span>
    <span class="btn btn-solid">MEMBER LOGIN</span>
  </div>
  <nav class="nav">
    <span class="active">HOME</span><span>ABOUT US</span><span>SERVICES</span><span>NEWS</span><span>TESTIMONIALS</span><span>CONTACT US</span>
  </nav>
</header>

<section class="hero" role="img" aria-label="Photo of people meeting around a table in a bright office">
  <div class="hero-copy">
    <h1>SERENIA</h1>
    <p>Your condo fees arrive on time, every month, no matter who is late. We handle the collection so managers can focus on the building.</p>
    <span class="btn btn-solid">READ MORE</span>
  </div>
  <div class="hero-dots"><i></i><i></i><i></i></div>
</section>

<section class="services">
  <h2 class="section-title">OUR <span>SERVICES</span></h2>
  <p class="section-sub">Steady revenue for your condominium, with calm and simple follow-up of overdue fees.</p>
  <div class="service-grid">
    <div class="service">
      <svg width="48" height="48" viewBox="0 0 48 48" fill="none" stroke="#1b2c5c" stroke-width="2"><rect x="8" y="12" width="32" height="24"/><path d="M8 18h32" stroke="#f36f21"/><circle cx="24" cy="27" r="5" stroke="#f36f21"/></svg>
      <h3>SED UT PERSPICIATIS</h3>
      <p>Guaranteed monthly transfer of all condo fees to the manager on a fixed date, regardless of defaults.</p>
      <span class="btn btn-outline">READ MORE</span>
    </div>
    <div class="service">
      <svg width="48" height="48" viewBox="0 0 48 48" fill="none" stroke="#1b2c5c" stroke-width="2"><rect x="6" y="14" width="36" height="20"/><path d="M18 30l12-12" stroke="#f36f21"/><circle cx="18" cy="19" r="2" stroke="#f36f21"/><circle cx="30" cy="29" r="2" stroke="#f36f21"/></svg>
      <h3>SED UT PERSPICIATIS</h3>
      <p>Respectful collection of overdue balances, keeping good relations between neighbours in the building.</p>
      <span class="btn btn-outline">READ MORE</span>
    </div>
    <div class="service">
      <svg width="48" height="48" viewBox="0 0 48 48" fill="none" stroke="#1b2c5c" stroke-width="2"><rect x="12" y="6" width="24" height="36"/><path d="M17 16h14M17 23h14M17 30h9" stroke="#f36f21"/></svg>
      <h3>SED UT PERSPICIATIS</h3>
      <p>Clear monthly reports for managers and residents, showing every payment and every pending balance.</p>
      <span class="btn btn-outline">READ MORE</span>
    </div>
  </div>
</section>

<section class="about">
  <div class="ph" role="img" aria-label="Photo of a business team seated around a meeting table"></div>
  <div class="about-copy">
    <h2>ABOUT <span>US</span></h2>
    <p>We partner with building managers to keep condominium budgets stable. Each month we advance the full expected fee income, then take care of late payers ourselves with patience and clear communication.</p>
    <p>Our team brings years of experience in property administration and fair collection practice. Managers gain certainty, residents gain a well kept home, and the whole building enjoys peace of mind.</p>
  </div>
</section>

<section class="video">
  <h2 class="section-title">OUR <span style="color:var(--white)">VIDEO</span></h2>
  <p class="section-sub">See how a guaranteed fee plan brings calm to managers and residents alike.</p>
  <div class="video-frame" role="img" aria-label="Video still of two colleagues shaking hands in an office">
    <svg width="60" height="60" viewBox="0 0 60 60"><circle cx="30" cy="30" r="28" fill="rgba(255,255,255,.35)" stroke="#fff" stroke-width="2"/><path d="M24 18l18 12-18 12z" fill="#fff"/></svg>
  </div>
</section>

<section class="what">
  <div class="what-copy">
    <h2>WHAT <span>WE DO</span></h2>
    <p>We review the building's fee schedule, agree on a payment date and transfer the full amount on that day every month. From then on, any resident delay is our task, not the manager's.</p>
    <p>Residents receive friendly reminders and flexible plans, so balances are settled without conflict and the community stays a pleasant place to live.</p>
  </div>
  <div class="ph" role="img" aria-label="Photo of a small team discussing documents at a desk"></div>
</section>

<section class="news">
  <h2 class="section-title">LATEST <span>NEWS</span></h2>
  <p class="section-sub">Articles and updates on condominium management and fee planning.</p>
  <div class="news-grid">
    <article class="card">
      <div class="ph" role="img" aria-label="Photo of a meeting around a conference table"></div>
      <div class="card-body"><small>02 MARCH 2019</small><h4>SED UT PERSPICIATIS UNDE OMNIS ISTE NATUS ERROR SIT</h4><p>Five simple steps to keep your building budget on track through the year.</p><span class="btn btn-outline">READ MORE</span></div>
    </article>
    <article class="card">
      <div class="ph" role="img" aria-label="Photo of colleagues working together at a long table"></div>
      <div class="card-body"><small>02 MARCH 2019</small><h4>SED UT PERSPICIATIS UNDE OMNIS ISTE NATUS ERROR SIT</h4><p>How fair reminders help residents settle balances without tension.</p><span class="btn btn-outline">READ MORE</span></div>
    </article>
    <article class="card">
      <div class="ph" role="img" aria-label="Photo of an open plan office with people at desks"></div>
      <div class="card-body"><small>02 MARCH 2019</small><h4>SED UT PERSPICIATIS UNDE OMNIS ISTE NATUS ERROR SIT</h4><p>What managers should ask before signing a fee guarantee plan.</p><span class="btn btn-outline">READ MORE</span></div>
    </article>
  </div>
</section>

<section class="testimonials">
  <h2 class="section-title">OUR <span>TESTIMONIALS</span></h2>
  <p class="section-sub">What building managers and residents say about working with us.</p>
  <div class="quote-grid">
    <div class="quote">
      <div class="quote-box"><span class="stars"><b>“</b>★★★★★</span>Since we joined, the fee income arrives on the same day every month. I no longer chase late payers and our maintenance plan finally runs on schedule.</div>
      <div class="author"><div class="avatar" role="img" aria-label="Portrait photo placeholder"></div><div><h4>NORA HALE</h4><small>Posted on 12 Jan 2019</small></div></div>
    </div>
    <div class="quote">
      <div class="quote-box"><span class="stars"><b>“</b>★★★★★</span>Our building feels calmer. Repairs happen quickly and neighbours are kinder now that money talk is handled by a professional and friendly team.</div>
      <div class="author"><div class="avatar" role="img" aria-label="Portrait photo placeholder"></div><div><h4>EVAN PRICE</h4><small>Posted on 12 Jan 2019</small></div></div>
    </div>
  </div>
</section>

<section class="location">
  <div class="map" role="img" aria-label="Street map showing the office location"></div>
  <div class="map-card"><h4>SERENIA</h4><p>48 Harbor Lane, Springfield, ST 00000</p></div>
  <div class="photo" role="img" aria-label="Photo of the office interior with staff at work"></div>
</section>

<footer class="site-footer">
  <div class="footer-cols">
    <div class="footer-col col-contact">
      <h4>CONTACT US</h4>
      <div class="contact-line"><svg width="14" height="18" viewBox="0 0 24 30" fill="#f36f21"><path d="M12 0a10 10 0 0 0-10 10c0 8 10 20 10 20s10-12 10-20A10 10 0 0 0 12 0zm0 14a4 4 0 1 1 0-8 4 4 0 0 1 0 8z"/></svg><span>48 Harbor Lane, Springfield, ST 00000</span></div>
      <div class="contact-line"><svg width="14" height="14" viewBox="0 0 24 24" fill="#f36f21"><path d="M6.6 10.8a15 15 0 0 0 6.6 6.6l2.2-2.2c.3-.3.7-.4 1-.2 1.1.4 2.3.6 3.6.6.6 0 1 .4 1 1V20c0 .6-.4 1-1 1A17 17 0 0 1 3 4c0-.6.4-1 1-1h3.5c.6 0 1 .4 1 1 0 1.3.2 2.5.6 3.6.1.3 0 .7-.2 1z"/></svg><span>(555) 013-4782</span></div>
      <div class="contact-line"><svg width="14" height="14" viewBox="0 0 24 24" fill="none" stroke="#f36f21" stroke-width="2"><rect x="2" y="5" width="20" height="14"/><path d="M2 5l10 8 10-8"/></svg><span>hello@serenia-example.com</span></div>
    </div>
    <div class="footer-col col-links">
      <h4>QUICK LINKS</h4>
      <ul><li>Home</li><li>About Us</li><li>Services</li><li>News</li><li>Contact Us</li></ul>
    </div>
    <div class="footer-col col-res">
      <h4>RESOURCE</h4>
      <ul><li>Fee planning guide</li><li>Manager handbook</li><li>Resident FAQ</li><li>Payment options</li><li>Annual reports</li></ul>
    </div>
    <div class="footer-col col-news">
      <h4>NEWSLETTER SUBSCRIPTION</h4>
      <p>Register your email address to get more information about us.</p>
      <div class="newsletter-input">Email Address</div>
      <span class="btn btn-solid">SUBSCRIBE</span>
    </div>
  </div>
  <div class="socials"><i></i><i></i><i></i><i></i></div>
  <div class="copyright">Copyrights © 2019 Serenia. All Rights Reserved</div>
</footer>

</body>
</html>
```